Veterinary company needs powerpoint design

Our veterinary company working with in vitro fertilization needs a professional power point design and business card design.
for the power point desing we would like frontpage, plain slides, table slides, figure slides etc.
the colours should be matching our logo in blue-ish: blue, purple, grey, turquoise
We like it minimalistic, elegant, serious but with a warm touch.

Target Market(s)

Academic,

Industry/Entity Type

Veterinary

Contact Information for Business Card

name, title, email, phone, website

Font styles to use
Sans Serif

Colors
0455a3
3277b5
85abd2
cfdeed
6b449b
886aae
b8a6cd
e4daeb
86cfc6

```html
<!DOCTYPE html>
<html lang="en">
<head>
<meta charset="utf-8">
<title>ALMBERG BioRepro Labs – Presentation and Business Card</title>
<link rel="stylesheet" href="https://fonts.googleapis.com/css2?family=Open+Sans:wght@300;400;600;700;800&display=swap">
<style>
:root{
  --blue:#0455a3;--blue2:#3277b5;--blue3:#85abd2;--blue4:#cfdeed;
  --purple:#6b449b;--purple2:#886aae;--purple3:#b8a6cd;--purple4:#e4daeb;
  --teal:#86cfc6;--navy:#1c4f8c;--ink:#2b2b2b;--grey:#777;--line:#d9d9d9;
  --backdrop:#6e1418;--band:#e6e6e6;
}
*{box-sizing:border-box;margin:0;padding:0}
html,body{width:1200px;height:2419px;overflow:hidden}
body{position:relative;background:var(--backdrop);font-family:"Open Sans",Arial,sans-serif;color:var(--ink)}
.deck{position:absolute;left:8px;top:8px;display:grid;grid-template-columns:repeat(3,390px);grid-auto-rows:219px;gap:6px 7px}
.deck-last{position:absolute;left:202px;top:1808px;display:flex;gap:7px}
.slide{position:relative;width:390px;height:219px;background:#fff;overflow:hidden}
.slide .tab{position:absolute;top:0;left:50%;width:90px;height:5px;background:var(--navy);transform:translateX(-50%)}
.slide .title{position:absolute;top:10px;left:0;right:0;text-align:center;font-size:14px;font-weight:700;color:var(--ink)}
.mark{position:absolute;left:10px;bottom:7px;font-size:7px;font-weight:700;color:var(--navy);letter-spacing:.5px;display:flex;align-items:center;gap:3px}
.mark i{display:block;width:6px;height:6px;border-radius:50%;background:var(--blue2)}
.pg{position:absolute;right:14px;bottom:7px;width:18px;height:7px;border:1px solid var(--line);border-radius:4px;font-size:4px;text-align:center;line-height:5px;color:var(--grey)}
.abs{position:absolute}
.t{font-size:5px;line-height:1.4;color:#666}
.h{font-size:6px;font-weight:700;color:#333}
.photo{position:absolute}
table.data{border-collapse:collapse;font-size:4.5px;color:#555}
table.data td,table.data th{border:1px solid #e2e2e2;padding:2px 4px;text-align:center}
table.data th{color:#fff;font-weight:600}
.icon-sq{position:absolute;border:1px solid var(--line);background:#fff;display:flex;align-items:center;justify-content:center}
.pill{position:absolute;border-radius:10px;font-size:5px;color:#fff;padding:3px 8px}
.band{position:absolute;left:0;top:2036px;width:1200px;height:383px;background:var(--band)}
.card{position:absolute;width:548px;height:323px;background:#fff;overflow:hidden}
</style>
</head>
<body>

<div class="deck">

<!-- 1 Cover -->
<section class="slide cover">
  <div class="photo" role="img" aria-label="Faint horse photograph under a blue tint" style="inset:0;background:linear-gradient(135deg,#2a6cb0,#3f82c2 60%,#2a62a3)"></div>
  <div class="abs" style="left:0;right:0;top:50px;text-align:center;color:#fff;font-size:19px;font-weight:700">Your Slides Deck Name</div>
  <div class="abs" style="left:0;right:0;top:75px;text-align:center;color:#fff;font-size:9px">Your Slides Deck Name</div>
  <div class="abs" style="left:0;right:0;bottom:0;height:90px;background:#fff"></div>
  <div class="abs" style="left:18px;bottom:38px;font-size:10px;font-weight:700;color:var(--navy);display:flex;align-items:center;gap:4px"><i style="display:block;width:9px;height:9px;border-radius:50%;background:var(--blue2)"></i>ALMBERG</div>
  <div class="abs" style="left:18px;bottom:30px;font-size:5px;color:var(--navy)">BioRepro Labs</div>
  <div class="pg">1</div>
</section>

<!-- 2 Section The Company -->
<section class="slide">
  <div class="photo" role="img" aria-label="Photograph of three horses in a green pasture" style="inset:0;background:linear-gradient(180deg,#b9c6c9 0%,#8c7a68 35%,#6a4a33 60%,#6f8a4c 90%)"></div>
  <div class="abs" style="left:100px;right:0;top:70px;height:56px;background:rgba(50,119,181,.88)"></div>
  <div class="abs" style="left:115px;top:80px;color:#fff;font-size:26px;font-weight:700">01</div>
  <div class="abs" style="left:165px;top:82px;color:#fff;font-size:11px;line-height:1.2">THE<br>COMPANY</div>
  <div class="abs" style="left:165px;top:111px;color:#fff;font-size:4.5px">This is the subtitle that makes it comprehensive</div>
</section>

<!-- 3 Section Our Services -->
<section class="slide">
  <div class="photo" role="img" aria-label="Photograph of a brown horse in a sunny meadow" style="inset:0;background:linear-gradient(180deg,#a9b8a4 0%,#9a6a3f 40%,#7e4a28 60%,#8aa256 90%)"></div>
  <div class="abs" style="left:100px;right:0;top:70px;height:56px;background:rgba(50,119,181,.88)"></div>
  <div class="abs" style="left:115px;top:80px;color:#fff;font-size:26px;font-weight:700">02</div>
  <div class="abs" style="left:165px;top:82px;color:#fff;font-size:11px;line-height:1.2">OUR<br>SERVICES</div>
  <div class="abs" style="left:165px;top:111px;color:#fff;font-size:4.5px">This is the subtitle that makes it comprehensive</div>
</section>

<!-- 4 Plain text -->
<section class="slide">
  <div class="tab"></div><div class="title">Lorem ipsum dolor sit amet</div>
  <div class="abs" style="left:20px;right:20px;top:42px;height:140px;background:#f0f0f0"></div>
  <div class="abs" style="left:375px;top:50px;width:15px;height:140px;background:var(--blue)"></div>
  <div class="abs" style="left:0;top:185px;width:18px;height:6px;background:var(--blue)"></div>
  <div class="abs t" style="left:30px;top:52px;width:100px">Lorem ipsum dolor sit amet, consectetur adipiscing elit, sed do eiusmod tempor incididunt ut labore et dolore magna aliqua. Ut enim ad minim veniam, quis nostrud exercitation ullamco.<br><br>Lorem ipsum dolor sit amet, consectetur adipiscing elit, sed do eiusmod tempor incididunt ut labore et dolore magna aliqua.</div>
  <div class="abs t" style="left:143px;top:52px;width:100px">Lorem ipsum dolor sit amet, consectetur adipiscing elit, sed do eiusmod tempor incididunt ut labore et dolore magna aliqua. Ut enim ad minim veniam, quis nostrud exercitation ullamco.<br><br>Lorem ipsum dolor sit amet, consectetur adipiscing elit, sed do eiusmod tempor incididunt.</div>
  <div class="abs t" style="left:256px;top:52px;width:100px">Lorem ipsum dolor sit amet, consectetur adipiscing elit, sed do eiusmod tempor incididunt ut labore et dolore magna aliqua. Ut enim ad minim veniam, quis nostrud exercitation ullamco.<br><br>Lorem ipsum dolor sit amet, consectetur adipiscing elit, sed do eiusmod tempor.</div>
  <div class="mark"><i></i>ALMBERG</div><div class="pg">4</div>
</section>

<!-- 5 Icon grid with list -->
<section class="slide">
  <div class="tab"></div><div class="title">Lorem ipsum dolor sit amet</div>
  <div class="icon-sq" style="left:40px;top:48px;width:44px;height:44px"><svg width="16" height="14"><rect x="1" y="8" width="3" height="5" fill="#aaa"/><rect x="6" y="5" width="3" height="8" fill="#aaa"/><rect x="11" y="2" width="3" height="11" fill="#aaa"/></svg></div>
  <div class="icon-sq" style="left:90px;top:48px;width:44px;height:44px;background:var(--purple3);border-color:var(--purple3)"><svg width="16" height="14"><rect x="2" y="2" width="12" height="10" fill="none" stroke="#fff" stroke-width="1.5"/></svg></div>
  <div class="icon-sq" style="left:40px;top:98px;width:44px;height:44px"><svg width="16" height="14"><path d="M3 2h10v4a5 5 0 0 1-10 0z" fill="#aaa"/><rect x="6" y="11" width="4" height="2" fill="#aaa"/></svg></div>
  <div class="icon-sq" style="left:90px;top:98px;width:44px;height:44px"><svg width="16" height="14"><path d="M1 2h3l2 8h8l1-6H5" fill="none" stroke="#aaa" stroke-width="1.4"/></svg></div>
  <div class="abs" style="left:150px;top:52px;width:0;height:0;border-left:7px solid #bbb;border-top:4px solid transparent;border-bottom:4px solid transparent;box-shadow:none"></div>
  <div class="abs" style="left:150px;top:78px;width:0;height:0;border-left:7px solid var(--purple2);border-top:4px solid transparent;border-bottom:4px solid transparent"></div>
  <div class="abs" style="left:150px;top:104px;width:0;height:0;border-left:7px solid #bbb;border-top:4px solid transparent;border-bottom:4px solid transparent"></div>
  <div class="abs" style="left:150px;top:130px;width:0;height:0;border-left:7px solid #bbb;border-top:4px solid transparent;border-bottom:4px solid transparent"></div>
  <div class="abs" style="left:150px;top:156px;width:0;height:0;border-left:7px solid #bbb;border-top:4px solid transparent;border-bottom:4px solid transparent"></div>
  <div class="abs t" style="left:165px;top:48px;width:150px"><b>Add Contents Title</b><br>You can simply impress your audience and add a unique zing.</div>
  <div class="abs t" style="left:165px;top:74px;width:150px"><b>Add Contents Title</b><br>You can simply impress your audience and add a unique zing.</div>
  <div class="abs t" style="left:165px;top:100px;width:150px"><b>Add Contents Title</b><br>You can simply impress your audience and add a unique zing.</div>
  <div class="abs t" style="left:165px;top:126px;width:150px"><b>Add Contents Title</b><br>You can simply impress your audience and add a unique zing.</div>
  <div class="abs t" style="left:165px;top:152px;width:150px"><b>Add Contents Title</b><br>You can simply impress your audience and add a unique zing.</div>
  <div class="mark"><i></i>ALMBERG</div><div class="pg">5</div>
</section>

<!-- 6 Purple feature -->
<section class="slide">
  <svg class="abs" style="left:0;top:0" width="150" height="219"><polygon points="10,20 150,20 150,35 130,35 130,219 10,219" fill="var(--purple3)"/><polygon points="130,0 150,20 130,20" fill="var(--purple)"/></svg>
  <div class="abs" style="left:40px;top:90px;width:50px;height:50px;border-radius:50%;background:#fff;display:flex;align-items:center;justify-content:center"><svg width="22" height="26"><rect x="2" y="3" width="16" height="20" rx="1" fill="none" stroke="#333" stroke-width="1.6"/><rect x="6" y="1" width="8" height="4" fill="#333"/><line x1="5" y1="10" x2="14" y2="10" stroke="#333"/><line x1="5" y1="14" x2="12" y2="14" stroke="#333"/><circle cx="17" cy="20" r="5" fill="#333"/><path d="M14.5 20l2 2 3-3.5" stroke="#fff" fill="none"/></svg></div>
  <div class="abs" style="left:155px;top:24px;font-size:13px;font-weight:700">Lorem ipsum dolor sit amet</div>
  <div class="abs t" style="left:155px;top:46px;width:215px">Lorem ipsum dolor sit amet, consectetur adipiscing elit, sed do eiusmod tempor incididunt ut labore et dolore magna aliqua. Ut enim ad minim veniam, quis nostrud exercitation ullamco laboris nisi ut aliquip ex ea commodo consequat. Duis aute irure dolor in reprehenderit in voluptate velit esse.</div>
  <div class="abs t" style="left:155px;top:110px;width:215px">Lorem ipsum dolor sit amet, consectetur adipiscing elit, sed do eiusmod tempor incididunt ut labore et dolore magna aliqua. Ut enim ad minim veniam, quis nostrud exercitation ullamco laboris nisi ut aliquip ex ea commodo consequat. Duis aute irure dolor in reprehenderit.</div>
  <div class="pg">6</div>
</section>

<!-- 7 Services photos -->
<section class="slide">
  <div class="tab"></div><div class="title">Lorem ipsum dolor sit amet</div>
  <div class="photo" role="img" aria-label="Black and white photo of a handshake" style="left:20px;top:60px;width:78px;height:60px;background:linear-gradient(135deg,#d8d8d8,#555)"></div>
  <div class="photo" role="img" aria-label="Black and white photo of documents on a desk" style="left:110px;top:60px;width:78px;height:60px;background:linear-gradient(135deg,#eee,#888)"></div>
  <div class="photo" role="img" aria-label="Black and white photo of a person at work" style="left:200px;top:60px;width:78px;height:60px;background:linear-gradient(135deg,#ccc,#666)"></div>
  <div class="photo" role="img" aria-label="Black and white photo of hands typing on a laptop" style="left:290px;top:60px;width:78px;height:60px;background:linear-gradient(135deg,#bbb,#333)"></div>
  <div class="abs" style="left:20px;top:126px;width:78px;text-align:center;font-size:5.5px;font-weight:700;color:var(--blue2)">SERVICE ONE</div>
  <div class="abs" style="left:110px;top:126px;width:78px;text-align:center;font-size:5.5px;font-weight:700;color:var(--purple)">SERVICE TWO</div>
  <div class="abs" style="left:200px;top:126px;width:78px;text-align:center;font-size:5.5px;font-weight:700;color:#444">SERVICE THREE</div>
  <div class="abs" style="left:290px;top:126px;width:78px;text-align:center;font-size:5.5px;font-weight:700;color:var(--purple2)">SERVICE FOUR</div>
  <div class="abs t" style="left:20px;top:134px;width:78px;text-align:center">You can simply impress your audience and add a zing.</div>
  <div class="abs t" style="left:110px;top:134px;width:78px;text-align:center">You can simply impress your audience and add a zing.</div>
  <div class="abs t" style="left:200px;top:134px;width:78px;text-align:center">You can simply impress your audience and add a zing.</div>
  <div class="abs t" style="left:290px;top:134px;width:78px;text-align:center">You can simply impress your audience and add a zing.</div>
  <div class="mark"><i></i>ALMBERG</div><div class="pg">7</div>
</section>

<!-- 8 Banner tables -->
<section class="slide">
  <div class="tab"></div><div class="title">Lorem ipsum dolor sit amet</div>
  <div class="abs" style="left:30px;top:44px;width:330px;height:60px;border:1.5px solid var(--purple3);border-radius:6px"></div>
  <div class="pill" style="left:38px;top:38px;background:var(--purple2);border-radius:2px">Your Text Here</div>
  <div class="abs t" style="left:40px;top:56px;width:110px"><b>Your Text Here</b><br>Get a modern PowerPoint Presentation that is beautifully designed. Easy to change colors.</div>
  <table class="data abs" style="left:200px;top:52px;width:150px"><tr><th style="background:var(--purple2)">Text</th><th style="background:var(--purple2)">Text</th><th style="background:var(--purple2)">Text</th><th style="background:var(--purple2)">Text</th></tr><tr><td>Add Text</td><td>Text</td><td>Text</td><td>Text</td></tr><tr><td>Add Text</td><td>Text</td><td>Text</td><td>Text</td></tr><tr><td>Add Text</td><td>Text</td><td>Text</td><td>Text</td></tr></table>
  <div class="abs" style="left:30px;top:118px;width:330px;height:60px;border:1.5px solid var(--teal);border-radius:6px"></div>
  <div class="pill" style="left:38px;top:112px;background:var(--teal);border-radius:2px">Your Text Here</div>
  <div class="abs t" style="left:40px;top:130px;width:110px"><b>Your Text Here</b><br>Get a modern PowerPoint Presentation that is beautifully designed. Easy to change colors.</div>
  <table class="data abs" style="left:200px;top:126px;width:150px"><tr><th style="background:var(--teal)">Text</th><th style="background:var(--teal)">Text</th><th style="background:var(--teal)">Text</th><th style="background:var(--teal)">Text</th></tr><tr><td>Add Text</td><td>Text</td><td>Text</td><td>Text</td></tr><tr><td>Add Text</td><td>Text</td><td>Text</td><td>Text</td></tr><tr><td>Add Text</td><td>Text</td><td>Text</td><td>Text</td></tr></table>
  <div class="mark"><i></i>ALMBERG</div><div class="pg">8</div>
</section>

<!-- 9 Environmental pie -->
<section class="slide">
  <div class="tab"></div><div class="title">Environmental Pie Chart</div>
  <svg class="abs" style="left:40px;top:45px" width="130" height="130" viewBox="0 0 130 130">
    <g transform="rotate(-90 65 65)" fill="none" stroke-width="18">
      <circle cx="65" cy="65" r="50" stroke="var(--teal)" stroke-dasharray="110 204"/>
      <circle cx="65" cy="65" r="50" stroke="var(--purple3)" stroke-dasharray="0 110 140 64"/>
      <circle cx="65" cy="65" r="50" stroke="var(--blue3)" stroke-dasharray="0 250 64 0"/>
    </g>
    <circle cx="65" cy="65" r="24" fill="none" stroke="var(--purple2)" stroke-width="1.5"/>
    <circle cx="65" cy="62" r="9" fill="none" stroke="var(--purple2)" stroke-width="1.5"/>
  </svg>
  <div class="abs" style="left:220px;top:58px;width:22px;height:22px;border-radius:50%;background:var(--teal);color:#fff;font-size:7px;font-weight:700;text-align:center;line-height:22px">60%</div>
  <div class="abs" style="left:220px;top:98px;width:22px;height:22px;border-radius:50%;background:var(--purple3);color:#fff;font-size:7px;font-weight:700;text-align:center;line-height:22px">30%</div>
  <div class="abs" style="left:220px;top:138px;width:22px;height:22px;border-radius:50%;background:var(--blue3);color:#fff;font-size:7px;font-weight:700;text-align:center;line-height:22px">20%</div>
  <div class="abs t" style="left:250px;top:56px;width:110px"><b>Your Title.</b><br>Lorem ipsum dolor sit amet, consectetur adipiscing elit, sed do eiusmod tempor.</div>
  <div class="abs t" style="left:250px;top:96px;width:110px"><b>Your Title.</b><br>Lorem ipsum dolor sit amet, consectetur adipiscing elit, sed do eiusmod tempor.</div>
  <div class="abs t" style="left:250px;top:136px;width:110px"><b>Your Title.</b><br>Lorem ipsum dolor sit amet, consectetur adipiscing elit, sed do eiusmod tempor.</div>
  <div class="mark"><i></i>ALMBERG</div><div class="pg">9</div>
</section>

<!-- 10 Our Services panel -->
<section class="slide">
  <div class="tab"></div><div class="title">Our Services</div>
  <div class="abs" style="left:20px;top:60px;width:350px;height:120px;background:var(--purple2)"></div>
  <div class="abs" style="left:30px;top:68px;width:100px;color:#fff;font-size:6px;font-style:italic">A title for your slide</div>
  <div class="abs" style="left:145px;top:68px;width:100px;color:#fff;font-size:6px;font-style:italic">A title for your slide</div>
  <div class="abs" style="left:260px;top:68px;width:100px;color:#fff;font-size:6px;font-style:italic">A title for your slide</div>
  <div class="abs t" style="left:30px;top:80px;width:100px;color:#efe8f5">Lorem ipsum dolor sit amet, consectetur adipiscing elit, sed do eiusmod tempor incididunt ut labore et dolore magna aliqua.</div>
  <div class="abs t" style="left:145px;top:80px;width:100px;color:#efe8f5">Lorem ipsum dolor sit amet, consectetur adipiscing elit, sed do eiusmod tempor incididunt ut labore et dolore magna aliqua.</div>
  <div class="abs t" style="left:260px;top:80px;width:100px;color:#efe8f5">Lorem ipsum dolor sit amet, consectetur adipiscing elit, sed do eiusmod tempor incididunt ut labore et dolore magna aliqua.</div>
  <div class="abs" style="left:68px;top:156px;width:16px;height:16px;border-radius:50%;background:#fff"></div>
  <div class="abs" style="left:183px;top:156px;width:16px;height:16px;border-radius:50%;background:#fff"></div>
  <div class="abs" style="left:298px;top:156px;width:16px;height:16px;border-radius:50%;background:#fff"></div>
  <svg class="abs" style="left:68px;top:156px" width="16" height="16"><path d="M8 4a3 3 0 0 1 3 3c0 2-3 5-3 5s-3-3-3-5a3 3 0 0 1 3-3z" fill="#333"/></svg>
  <svg class="abs" style="left:183px;top:156px" width="16" height="16"><rect x="4" y="5" width="8" height="6" fill="none" stroke="#333"/></svg>
  <svg class="abs" style="left:298px;top:156px" width="16" height="16"><circle cx="8" cy="8" r="4" fill="none" stroke="#333"/><line x1="5" y1="11" x2="11" y2="5" stroke="#333"/></svg>
  <div class="mark"><i></i>ALMBERG</div><div class="pg">10</div>
</section>

<!-- 11 Pie with list -->
<section class="slide">
  <div class="tab"></div><div class="title">Lorem ipsum dolor sit amet</div>
  <div class="abs" style="left:20px;top:40px;width:140px;font-size:7px;color:#333;line-height:1.3">This is a sample text. You can replace this text. Enter Your text Here.</div>
  <svg class="abs" style="left:25px;top:72px" width="130" height="100" viewBox="0 0 130 100">
    <ellipse cx="65" cy="56" rx="55" ry="36" fill="#14477c"/>
    <g transform="translate(65 50) scale(1 .65) rotate(-90)" fill="none" stroke-width="55">
      <circle r="27.5" stroke="var(--blue)" stroke-dasharray="86 173"/>
      <circle r="27.5" stroke="var(--blue2)" stroke-dasharray="0 86 60 113"/>
      <circle r="27.5" stroke="var(--blue3)" stroke-dasharray="0 146 45 68"/>
      <circle r="27.5" stroke="var(--blue4)" stroke-dasharray="0 191 68 0"/>
    </g>
  </svg>
  <div class="abs t" style="left:30px;top:180px;font-size:4px">■ 1st Qtr &nbsp; ■ 2nd Qtr &nbsp; ■ 3rd Qtr &nbsp; ■ 4th Qtr</div>
  <div class="pill" style="left:205px;top:46px;width:160px;background:var(--blue2)">This is a sample text. Enter Your text Here</div>
  <div class="pill" style="left:205px;top:72px;width:160px;background:var(--blue)">This is a sample text. Enter Your text Here</div>
  <div class="pill" style="left:205px;top:98px;width:160px;background:var(--blue3)">This is a sample text. Enter Your text Here</div>
  <div class="pill" style="left:205px;top:124px;width:160px;background:var(--teal)">This is a sample text. Enter Your text Here</div>
  <div class="pill" style="left:205px;top:150px;width:160px;background:var(--blue2)">This is a sample text. Enter Your text Here</div>
  <div class="abs" style="left:190px;top:44px;width:14px;height:14px;border-radius:50%;border:1.5px solid var(--blue2);background:#fff"></div>
  <div class="abs" style="left:190px;top:70px;width:14px;height:14px;border-radius:50%;border:1.5px solid var(--blue);background:#fff"></div>
  <div class="abs" style="left:190px;top:96px;width:14px;height:14px;border-radius:50%;border:1.5px solid var(--blue3);background:#fff"></div>
  <div class="abs" style="left:190px;top:122px;width:14px;height:14px;border-radius:50%;border:1.5px solid var(--teal);background:#fff"></div>
  <div class="abs" style="left:190px;top:148px;width:14px;height:14px;border-radius:50%;border:1.5px solid var(--blue2);background:#fff"></div>
  <div class="mark"><i></i>ALMBERG</div><div class="pg">11</div>
</section>

<!-- 12 Sample text with microscope -->
<section class="slide">
  <div class="tab"></div><div class="title">Lorem ipsum dolor sit amet</div>
  <div class="abs" style="left:30px;top:46px;width:130px;height:130px;border-radius:50%;background:var(--purple3)"></div>
  <div class="abs" style="left:30px;top:85px;width:130px;text-align:center;color:#fff;font-size:12px;font-weight:700">SAMPLE TEXT</div>
  <div class="abs t" style="left:48px;top:103px;width:94px;text-align:center;color:#fff">Lorem ipsum dolor sit amet, consectetur adipiscing elit, sed do eiusmod tempor incididunt ut labore.</div>
  <div class="photo" role="img" aria-label="Illustration of a laboratory microscope" style="left:220px;top:50px;width:120px;height:130px;background:radial-gradient(circle at 60% 45%,#d9dde3,#f4f5f7 70%);border-radius:4px"></div>
  <div class="mark"><i></i>ALMBERG</div><div class="pg">12</div>
</section>

<!-- 13 Steps -->
<section class="slide">
  <div class="tab"></div><div class="title">Lorem ipsum dolor sit amet</div>
  <svg class="abs" style="left:0;top:40px" width="390" height="150">
    <polygon points="110,0 230,0 210,28 90,28" fill="var(--blue2)"/>
    <polygon points="135,32 255,32 235,60 115,60" fill="var(--blue3)"/>
    <polygon points="160,64 280,64 260,92 140,92" fill="var(--blue2)"/>
    <polygon points="185,96 305,96 285,124 165,124" fill="var(--blue3)"/>
  </svg>
  <div class="abs" style="left:118px;top:48px;color:#fff;font-size:6px;width:100px">Insert your desired text here</div>
  <div class="abs" style="left:143px;top:80px;color:#fff;font-size:6px;width:100px">Insert your desired text here</div>
  <div class="abs" style="left:168px;top:112px;color:#fff;font-size:6px;width:100px">Insert your desired text here</div>
  <div class="abs" style="left:193px;top:144px;color:#fff;font-size:6px;width:100px">Insert your desired text here</div>
  <div class="abs" style="left:62px;top:44px;color:var(--navy);font-size:14px;font-weight:700;line-height:1">1<div style="font-size:5px;color:#555;font-weight:400">Edit Text</div></div>
  <div class="abs" style="left:87px;top:76px;color:var(--navy);font-size:14px;font-weight:700;line-height:1">2<div style="font-size:5px;color:#555;font-weight:400">Edit Text</div></div>
  <div class="abs" style="left:112px;top:108px;color:var(--navy);font-size:14px;font-weight:700;line-height:1">3<div style="font-size:5px;color:#555;font-weight:400">Edit Text</div></div>
  <div class="abs" style="left:137px;top:140px;color:var(--navy);font-size:14px;font-weight:700;line-height:1">4<div style="font-size:5px;color:#555;font-weight:400">Edit Text</div></div>
  <div class="mark"><i></i>ALMBERG</div><div class="pg">13</div>
</section>

<!-- 14 Blue header checks -->
<section class="slide">
  <div class="abs" style="left:0;right:0;top:0;height:95px;background:var(--blue2)"></div>
  <div class="abs" style="left:20px;top:38px;color:#fff;font-size:12px;font-weight:700">Lorem ipsum dolor</div>
  <div class="abs t" style="left:140px;top:18px;width:230px;color:#e6eef7">Lorem ipsum dolor sit amet, consectetur adipiscing elit, sed do eiusmod tempor incididunt ut labore et dolore magna aliqua. Ut enim ad minim veniam, quis nostrud exercitation ullamco laboris nisi ut aliquip ex ea commodo consequat. Duis aute irure dolor in reprehenderit in voluptate velit.</div>
  <svg class="abs" style="left:55px;top:112px" width="14" height="14"><circle cx="7" cy="7" r="7" fill="var(--blue2)"/><path d="M4 7l2 2 4-4" stroke="#fff" fill="none" stroke-width="1.5"/></svg>
  <svg class="abs" style="left:215px;top:112px" width="14" height="14"><circle cx="7" cy="7" r="7" fill="var(--purple2)"/><path d="M4 7l2 2 4-4" stroke="#fff" fill="none" stroke-width="1.5"/></svg>
  <svg class="abs" style="left:55px;top:148px" width="14" height="14"><circle cx="7" cy="7" r="7" fill="var(--blue3)"/><path d="M4 7l2 2 4-4" stroke="#fff" fill="none" stroke-width="1.5"/></svg>
  <svg class="abs" style="left:215px;top:148px" width="14" height="14"><circle cx="7" cy="7" r="7" fill="var(--teal)"/><path d="M4 7l2 2 4-4" stroke="#fff" fill="none" stroke-width="1.5"/></svg>
  <div class="abs t" style="left:75px;top:108px;width:110px"><b>Lorem ipsum dolor</b><br>Lorem ipsum dolor sit amet, consectetur adipiscing elit, sed do.</div>
  <div class="abs t" style="left:235px;top:108px;width:110px"><b>Lorem ipsum dolor</b><br>Lorem ipsum dolor sit amet, consectetur adipiscing elit, sed do.</div>
  <div class="abs t" style="left:75px;top:144px;width:110px"><b>Lorem ipsum dolor</b><br>Lorem ipsum dolor sit amet, consectetur adipiscing elit, sed do.</div>
  <div class="abs t" style="left:235px;top:144px;width:110px"><b>Lorem ipsum dolor</b><br>Lorem ipsum dolor sit amet, consectetur adipiscing elit, sed do.</div>
  <div class="mark"><i></i>ALMBERG</div><div class="pg">14</div>
</section>

<!-- 15 Photo background cards -->
<section class="slide">
  <div class="photo" role="img" aria-label="Grey-toned photograph of a horse grazing" style="inset:0;background:linear-gradient(180deg,#7d7d7d,#9a9a9a 40%,#5f5f5f)"></div>
  <div class="abs" style="left:0;right:0;top:10px;text-align:center;color:#fff;font-size:14px;font-weight:700">Lorem ipsum dolor sit amet</div>
  <div class="abs" style="left:0;right:0;top:80px;height:30px;background:var(--teal)"></div>
  <div class="abs" style="left:15px;top:100px;width:108px;height:85px;background:#fff;border-radius:4px"></div>
  <div class="abs" style="left:141px;top:100px;width:108px;height:85px;background:#fff;border-radius:4px"></div>
  <div class="abs" style="left:267px;top:100px;width:108px;height:85px;background:#fff;border-radius:4px"></div>
  <div class="abs t" style="left:22px;top:108px;width:94px">Lorem ipsum dolor sit amet, consectetur adipiscing elit, sed do eiusmod tempor incididunt ut labore et dolore magna aliqua.</div>
  <div class="abs t" style="left:148px;top:108px;width:94px">Lorem ipsum dolor sit amet, consectetur adipiscing elit, sed do eiusmod tempor incididunt ut labore et dolore magna aliqua.</div>
  <div class="abs t" style="left:274px;top:108px;width:94px">Lorem ipsum dolor sit amet, consectetur adipiscing elit, sed do eiusmod tempor incididunt ut labore et dolore magna aliqua.</div>
  <svg class="abs" style="left:125px;top:135px" width="14" height="14"><rect width="14" height="14" fill="var(--teal)"/><path d="M5 3l4 4-4 4" stroke="#fff" fill="none" stroke-width="1.5"/></svg>
  <svg class="abs" style="left:251px;top:135px" width="14" height="14"><rect width="14" height="14" fill="var(--teal)"/><path d="M5 3l4 4-4 4" stroke="#fff" fill="none" stroke-width="1.5"/></svg>
</section>

<!-- 16 Two column with photo -->
<section class="slide">
  <div class="photo" role="img" aria-label="Photograph of a cow in a stable" style="left:0;top:0;width:70px;height:219px;background:linear-gradient(180deg,#9aa09e,#3f4442 60%,#7b807e)"></div>
  <div class="abs" style="left:55px;top:0;width:15px;height:219px;background:rgba(134,207,198,.8)"></div>
  <div class="abs" style="left:88px;top:10px;font-size:13px;font-weight:700">Lorem ipsum dolor sit amet</div>
  <div class="abs" style="left:88px;top:34px;color:var(--blue2);font-size:10px;font-weight:700">01</div>
  <div class="abs" style="left:240px;top:34px;color:var(--blue2);font-size:10px;font-weight:700">02</div>
  <div class="abs h" style="left:105px;top:35px;width:120px">Get a modern PowerPoint Presentation that is beautifully designed.</div>
  <div class="abs h" style="left:257px;top:35px;width:120px">Get a modern PowerPoint Presentation that is beautifully designed.</div>
  <div class="abs t" style="left:88px;top:58px;width:135px"><span style="color:var(--blue2)">PowerPoint Presentation Template</span><br>Get a modern PowerPoint Presentation that is beautifully designed. I hope and I believe that this Template will your Time, Money and Reputation. Easy to change colors, photos and text. You can simply impress your audience and add a unique zing and appeal to your Presentations.<br><br>You can simply impress your audience and add a unique zing.</div>
  <div class="abs t" style="left:240px;top:58px;width:135px"><span style="color:var(--blue2)">PowerPoint Presentation Template</span><br>Get a modern PowerPoint Presentation that is beautifully designed. I hope and I believe that this Template will your Time, Money and Reputation. Easy to change colors, photos and text. You can simply impress your audience and add a unique zing and appeal to your Presentations.<br><br>You can simply impress your audience and add a unique zing.</div>
  <div class="mark" style="left:80px"><i></i>ALMBERG</div><div class="pg">16</div>
</section>

<!-- 17 Process chevrons -->
<section class="slide">
  <div class="tab"></div><div class="title">Lorem ipsum dolor sit amet</div>
  <svg class="abs" style="left:60px;top:50px" width="16" height="16"><circle cx="8" cy="8" r="5" fill="none" stroke="#333" stroke-width="3" stroke-dasharray="2 2"/><circle cx="8" cy="8" r="2" fill="#333"/></svg>
  <svg class="abs" style="left:145px;top:50px" width="16" height="16"><ellipse cx="8" cy="8" rx="7" ry="3" fill="none" stroke="#333"/><ellipse cx="8" cy="8" rx="3" ry="7" fill="none" stroke="#333"/><circle cx="8" cy="8" r="1.5" fill="#333"/></svg>
  <svg class="abs" style="left:230px;top:50px" width="16" height="16"><path d="M6 1h4M7 1v5L3 14h10L9 6V1" fill="none" stroke="#333" stroke-width="1.3"/></svg>
  <svg class="abs" style="left:315px;top:50px" width="16" height="16"><path d="M14 2L6 6 3 12l6-3z" fill="#333"/></svg>
  <svg class="abs" style="left:20px;top:76px" width="350" height="24">
    <polygon points="0,0 80,0 88,12 80,24 0,24 8,12" fill="#fff" stroke="#bbb"/>
    <polygon points="86,0 166,0 174,12 166,24 86,24 94,12" fill="#fff" stroke="#bbb"/>
    <polygon points="172,0 252,0 260,12 252,24 172,24 180,12" fill="var(--purple3)"/>
    <polygon points="258,0 338,0 346,12 338,24 258,24 266,12" fill="#fff" stroke="#bbb"/>
  </svg>
  <div class="abs h" style="left:30px;top:85px;width:70px;text-align:center;font-size:5px">Contents Title</div>
  <div class="abs h" style="left:116px;top:85px;width:70px;text-align:center;font-size:5px">Contents Title</div>
  <div class="abs h" style="left:202px;top:85px;width:70px;text-align:center;font-size:5px;color:#fff">Contents Title</div>
  <div class="abs h" style="left:288px;top:85px;width:70px;text-align:center;font-size:5px">Contents Title</div>
  <div class="abs t" style="left:30px;top:110px;width:72px;text-align:center">Lorem ipsum dolor sit amet, consectetur adipiscing elit, sed do eiusmod tempor incididunt ut labore et dolore.</div>
  <div class="abs t" style="left:116px;top:110px;width:72px;text-align:center">Lorem ipsum dolor sit amet, consectetur adipiscing elit, sed do eiusmod tempor incididunt ut labore et dolore.</div>
  <div class="abs t" style="left:202px;top:110px;width:72px;text-align:center">Lorem ipsum dolor sit amet, consectetur adipiscing elit, sed do eiusmod tempor incididunt ut labore et dolore.</div>
  <div class="abs t" style="left:288px;top:110px;width:72px;text-align:center">Lorem ipsum dolor sit amet, consectetur adipiscing elit, sed do eiusmod tempor incididunt ut labore et dolore.</div>
  <div class="mark"><i></i>ALMBERG</div><div class="pg">17</div>
</section>

<!-- 18 Number table -->
<section class="slide">
  <div class="tab"></div><div class="title">Lorem ipsum dolor sit amet</div>
  <table class="data abs" style="left:20px;top:38px;width:350px;font-size:5px">
    <tr><th style="background:#fff"></th><th style="background:var(--blue)">Lorem ipsum dolor</th><th style="background:var(--blue2)">Lorem ipsum dolor</th><th style="background:var(--teal)">Lorem ipsum dolor</th><th style="background:var(--blue3)">Lorem ipsum dolor</th><th style="background:var(--purple)">Lorem ipsum dolor</th></tr>
    <tr style="background:#f2f2f2"><td style="text-align:left">Lorem ipsum dolor</td><td>23</td><td>45</td><td>4</td><td>4</td><td>34</td></tr>
    <tr><td style="text-align:left">Lorem ipsum dolor</td><td>234</td><td>75</td><td>4</td><td>4</td><td>66</td></tr>
    <tr style="background:#f2f2f2"><td style="text-align:left">Lorem ipsum dolor</td><td>55</td><td>75</td><td>64</td><td>6</td><td>44</td></tr>
    <tr><td style="text-align:left">Lorem ipsum dolor</td><td>88</td><td>45</td><td>4</td><td>4</td><td>34</td></tr>
    <tr style="background:#f2f2f2"><td style="text-align:left">Lorem ipsum dolor</td><td>78</td><td>84</td><td>44</td><td>8</td><td>23</td></tr>
    <tr><td style="text-align:left">Lorem ipsum dolor</td><td>56</td><td>46</td><td>44</td><td>3</td><td>55</td></tr>
  </table>
  <div class="mark"><i></i>ALMBERG</div><div class="pg">18</div>
</section>

<!-- 19 Plan -->
<section class="slide">
  <div class="photo" role="img" aria-label="Purple-tinted photograph of a landscape" style="left:0;top:0;width:130px;height:219px;background:linear-gradient(180deg,#a58cc4,#8a6aae 60%,#b8a6cd)"></div>
  <div class="abs" style="left:130px;top:0;width:20px;height:219px;background:var(--purple4)"></div>
  <div class="abs" style="left:12px;top:60px;color:#fff;font-size:15px;font-weight:800">PLAN</div>
  <div class="abs t" style="left:12px;top:82px;width:100px;color:#fff">Lorem ipsum dolor sit amet, consectetur adipiscing elit, sed do eiusmod tempor incididunt ut labore et dolore magna aliqua. Ut enim ad minim veniam quis nostrud.</div>
  <div class="abs" style="left:160px;top:18px;width:215px;font-size:8px;font-weight:700;line-height:1.3;color:#222">Lorem ipsum dolor sit amet, consectetur adipiscing elit, sed do eiusmod tempor incididunt ut labore et dolore magna aliqua. Ut enim ad minim veniam, quis nostrud exercitation ullamco laboris nisi ut aliquip ex ea commodo consequat.</div>
  <div class="abs t" style="left:160px;top:105px;width:100px"><b>Lorem ipsum dolor</b><br>Lorem ipsum dolor sit amet, sed do consectetur adipiscing elit.</div>
  <div class="abs t" style="left:270px;top:105px;width:100px"><b>Lorem ipsum dolor</b><br>Lorem ipsum dolor sit amet, sed do consectetur adipiscing elit.</div>
  <div class="abs t" style="left:160px;top:145px;width:100px"><b>Lorem ipsum dolor</b><br>Lorem ipsum dolor sit amet, sed do consectetur adipiscing elit.</div>
  <div class="abs t" style="left:270px;top:145px;width:100px"><b>Lorem ipsum dolor</b><br>Lorem ipsum dolor sit amet, sed do consectetur adipiscing elit.</div>
  <div class="pg">19</div>
</section>

<!-- 20 Quote -->
<section class="slide">
  <div class="abs" style="inset:0;background:linear-gradient(180deg,#2f66a3,#4a7fb8 60%,#3a6ea8)"></div>
  <div class="abs" style="left:45px;top:45px;width:300px;height:100px;border:1px solid rgba(255,255,255,.6)"></div>
  <div class="abs" style="left:60px;top:62px;width:270px;color:#fff;font-family:Georgia,serif;font-size:11px;font-style:italic;line-height:1.4">"This is a quote. Words full of wisdom that someone important said and can make the reader get inspired."</div>
  <div class="abs" style="left:200px;top:118px;color:#fff;font-size:7px">—SOMEONE FAMOUS</div>
  <div class="pg" style="border-color:rgba(255,255,255,.4);color:#fff">20</div>
</section>

<!-- 21 Clipboard chart -->
<section class="slide">
  <div class="tab"></div><div class="title">Lorem ipsum dolor sit amet</div>
  <div class="abs" style="left:10px;top:40px;width:160px;height:150px;background:var(--blue2)"></div>
  <div class="abs" style="left:18px;top:55px;width:62px;height:120px;border:1px solid rgba(255,255,255,.5)"></div>
  <div class="abs t" style="left:22px;top:58px;width:56px;color:#fff">Lorem ipsum dolor sit amet, consectetur adipiscing elit, sed do eiusmod tempor incididunt ut labore et dolore magna aliqua ut enim ad minim veniam quis nostrud.</div>
  <div class="abs t" style="left:88px;top:58px;width:75px;color:#fff">Lorem ipsum dolor sit amet, consectetur adipiscing elit, sed do eiusmod tempor incididunt ut labore et dolore magna aliqua. Ut enim ad minim veniam, quis nostrud exercitation ullamco laboris nisi ut aliquip.</div>
  <svg class="abs" style="left:190px;top:28px" width="180" height="180">
    <rect x="10" y="20" width="160" height="155" rx="10" fill="var(--blue3)"/>
    <rect x="20" y="30" width="140" height="140" fill="#fff"/>
    <rect x="65" y="12" width="50" height="16" rx="3" fill="var(--purple)"/>
    <line x1="30" y1="130" x2="150" y2="130" stroke="#ccc"/>
    <g><rect x="38" y="90" width="6" height="40" fill="var(--blue)"/><rect x="45" y="105" width="6" height="25" fill="var(--purple2)"/><rect x="52" y="75" width="6" height="55" fill="var(--teal)"/>
    <rect x="72" y="80" width="6" height="50" fill="var(--blue)"/><rect x="79" y="100" width="6" height="30" fill="var(--purple2)"/><rect x="86" y="70" width="6" height="60" fill="var(--teal)"/>
    <rect x="106" y="95" width="6" height="35" fill="var(--blue)"/><rect x="113" y="85" width="6" height="45" fill="var(--purple2)"/><rect x="120" y="60" width="6" height="70" fill="var(--teal)"/>
    <rect x="136" y="100" width="6" height="30" fill="var(--blue)"/><rect x="143" y="78" width="6" height="52" fill="var(--purple2)"/></g>
    <g font-size="4" fill="#777"><text x="36" y="137">Category 1</text><text x="70" y="137">Category 2</text><text x="104" y="137">Category 3</text><text x="134" y="137">Category 4</text></g>
  </svg>
  <div class="mark"><i></i>ALMBERG</div><div class="pg">21</div>
</section>

<!-- 22 Timeline curve -->
<section class="slide">
  <div class="tab"></div><div class="title">Lorem ipsum dolor sit amet</div>
  <svg class="abs" style="left:0;top:35px" width="390" height="160">
    <path d="M40 130 V100 a20 20 0 0 1 20-20 H120 a20 20 0 0 0 20-20 V40 a20 20 0 0 1 20-20 H200" fill="none" stroke="var(--blue2)" stroke-width="1.5"/>
    <path d="M200 20 H260 a20 20 0 0 0 20-20" fill="none" stroke="var(--teal)" stroke-width="1.5"/>
    <circle cx="40" cy="118" r="10" fill="#fff" stroke="var(--blue2)" stroke-width="1.5"/>
    <circle cx="130" cy="70" r="10" fill="#fff" stroke="var(--purple2)" stroke-width="1.5"/>
    <circle cx="290" cy="15" r="10" fill="#fff" stroke="var(--teal)" stroke-width="1.5"/>
    <path d="M40 112v10M36 116h8" stroke="var(--blue2)" stroke-width="1.5"/>
    <path d="M125 72h10l-2-5h-6z" fill="var(--purple2)"/>
    <circle cx="290" cy="15" r="4" fill="none" stroke="var(--teal)"/>
  </svg>
  <div class="pill" style="left:28px;top:48px;background:var(--teal);border-radius:2px">Your Text Here</div>
  <div class="abs t" style="left:28px;top:62px;width:90px">You can simply impress your audience and add a unique zing and appeal to your Presentations.</div>
  <div class="abs" style="left:95px;top:120px;font-size:6px;color:var(--blue2);font-weight:700">Your Text Here</div>
  <div class="abs t" style="left:150px;top:110px;width:70px">Get a modern PowerPoint Presentation that is beautifully designed.</div>
  <div class="abs" style="left:150px;top:90px;font-size:6px;color:var(--purple2);font-weight:700">Your Text Here</div>
  <div class="abs t" style="left:60px;top:165px;width:80px">Get a modern PowerPoint Presentation that is beautifully designed.</div>
  <div class="abs" style="left:305px;top:42px;font-size:6px;color:var(--teal);font-weight:700">Your Text Here</div>
  <div class="abs t" style="left:280px;top:55px;width:80px">Get a modern PowerPoint Presentation that is beautifully designed.</div>
  <div class="mark"><i></i>ALMBERG</div><div class="pg">22</div>
</section>

<!-- 23 Table with icon list -->
<section class="slide">
  <div class="tab"></div><div class="title">Lorem ipsum dolor sit amet</div>
  <table class="data abs" style="left:20px;top:40px;width:200px">
    <tr><th style="background:var(--navy)">Text Here</th><th style="background:var(--navy)">Text Here</th><th style="background:var(--navy)">Text Here</th><th style="background:var(--navy)">Text Here</th></tr>
    <tr><td>Add Text</td><td>Text Here</td><td>Text Here</td><td>Text Here</td></tr>
    <tr><td>Add Text</td><td>Text Here</td><td>Text Here</td><td>Text Here</td></tr>
    <tr><td>Add Text</td><td>Text Here</td><td>Text Here</td><td>Text Here</td></tr>
    <tr><td>Add Text</td><td>Text Here</td><td>Text Here</td><td>Text Here</td></tr>
    <tr><td>Add Text</td><td>Text Here</td><td>Text Here</td><td>Text Here</td></tr>
    <tr><td>Add Text</td><td>Text Here</td><td>Text Here</td><td>Text Here</td></tr>
    <tr><td>Add Text</td><td>Text Here</td><td>Text Here</td><td>Text Here</td></tr>
    <tr><td>Add Text</td><td>Text Here</td><td>Text Here</td><td>Text Here</td></tr>
    <tr><td>Add Text</td><td>Text Here</td><td>Text Here</td><td>Text Here</td></tr>
  </table>
  <div class="abs" style="left:238px;top:42px;width:16px;height:16px;border-radius:50%;border:1px solid #bbb"></div>
  <div class="abs" style="left:238px;top:78px;width:16px;height:16px;border-radius:50%;border:1px solid #bbb"></div>
  <div class="abs" style="left:238px;top:114px;width:16px;height:16px;border-radius:50%;border:1px solid #bbb"></div>
  <div class="abs" style="left:238px;top:150px;width:16px;height:16px;border-radius:50%;border:1px solid #bbb"></div>
  <div class="abs t" style="left:262px;top:40px;width:110px"><b>Content Here</b><br>You can simply impress your audience and add a unique zing.</div>
  <div class="abs t" style="left:262px;top:76px;width:110px"><b>Content Here</b><br>You can simply impress your audience and add a unique zing.</div>
  <div class="abs t" style="left:262px;top:112px;width:110px"><b>Content Here</b><br>You can simply impress your audience and add a unique zing.</div>
  <div class="abs t" style="left:262px;top:148px;width:110px"><b>Content Here</b><br>You can simply impress your audience and add a unique zing.</div>
  <div class="mark"><i></i>ALMBERG</div><div class="pg">23</div>
</section>

<!-- 24 Cycle -->
<section class="slide">
  <div class="tab"></div><div class="title">Lorem ipsum dolor sit amet</div>
  <svg class="abs" style="left:135px;top:40px" width="120" height="140" viewBox="0 0 120 140">
    <circle cx="60" cy="70" r="42" fill="none" stroke="#ddd" stroke-width="1"/>
    <circle cx="60" cy="70" r="16" fill="#fff" stroke="var(--blue2)" stroke-width="2"/>
    <circle cx="60" cy="70" r="7" fill="none" stroke="var(--blue2)" stroke-width="2"/>
    <circle cx="60" cy="28" r="10" fill="var(--blue2)"/>
    <circle cx="90" cy="40" r="10" fill="var(--blue)"/>
    <circle cx="102" cy="70" r="10" fill="var(--purple)"/>
    <circle cx="90" cy="100" r="10" fill="var(--blue3)"/>
    <circle cx="60" cy="112" r="10" fill="var(--purple2)"/>
    <circle cx="30" cy="100" r="10" fill="var(--teal)"/>
    <circle cx="18" cy="70" r="10" fill="var(--blue2)"/>
    <circle cx="30" cy="40" r="10" fill="var(--purple3)"/>
  </svg>
  <div class="abs t" style="left:30px;top:50px;width:100px;text-align:right"><b>Add Text</b><br>Get a modern PowerPoint Presentation.</div>
  <div class="abs t" style="left:30px;top:82px;width:100px;text-align:right"><b>Add Text</b><br>Get a modern PowerPoint Presentation.</div>
  <div class="abs t" style="left:30px;top:114px;width:100px;text-align:right"><b>Add Text</b><br>Get a modern PowerPoint Presentation.</div>
  <div class="abs t" style="left:30px;top:146px;width:100px;text-align:right"><b>Add Text</b><br>Get a modern PowerPoint Presentation.</div>
  <div class="abs t" style="left:262px;top:50px;width:100px"><b>Add Text</b><br>Get a modern PowerPoint Presentation.</div>
  <div class="abs t" style="left:262px;top:82px;width:100px"><b>Add Text</b><br>Get a modern PowerPoint Presentation.</div>
  <div class="abs t" style="left:262px;top:114px;width:100px"><b>Add Text</b><br>Get a modern PowerPoint Presentation.</div>
  <div class="abs t" style="left:262px;top:146px;width:100px"><b>Add Text</b><br>Get a modern PowerPoint Presentation.</div>
  <div class="mark"><i></i>ALMBERG</div><div class="pg">24</div>
</section>

</div>

<div class="deck-last">
<!-- 25 Progress -->
<section class="slide">
  <div class="tab"></div><div class="title">Lorem ipsum dolor sit amet</div>
  <div class="abs" style="left:15px;top:45px;width:200px;height:160px;border:1px solid var(--purple3);border-radius:8px"></div>
  <div class="pill" style="left:40px;top:38px;width:150px;text-align:center;background:var(--purple3);font-style:italic">Lorem ipsum dolor</div>
  <div class="abs t" style="left:25px;top:58px;width:180px">Lorem ipsum dolor sit amet, consectetur adipiscing elit, sed do eiusmod tempor incididunt ut labore et dolore magna aliqua. Ut enim ad minim veniam, quis nostrud exercitation ullamco laboris nisi ut aliquip ex ea commodo.</div>
  <table class="data abs" style="left:35px;top:100px;width:160px"><tr><th style="background:var(--navy)">Text</th><th style="background:var(--navy)">Text</th><th style="background:var(--navy)">Text</th><th style="background:var(--navy)">Text</th></tr><tr><td>Add Text</td><td>Text</td><td>Text</td><td>Text</td></tr><tr><td>Add Text</td><td>Text</td><td>Text</td><td>Text</td></tr><tr><td>Add Text</td><td>Text</td><td>Text</td><td>Text</td></tr><tr><td>Add Text</td><td>Text</td><td>Text</td><td>Text</td></tr></table>
  <div class="abs t" style="left:230px;top:76px">Insert Text Here</div>
  <div class="abs" style="left:230px;top:86px;width:130px;height:5px;background:#555"></div><div class="abs" style="left:230px;top:86px;width:95px;height:5px;background:var(--purple3)"></div><div class="abs" style="left:352px;top:80px;font-size:4px;background:#333;color:#fff;padding:1px 2px">75%</div>
  <div class="abs t" style="left:230px;top:104px">Insert Text Here</div>
  <div class="abs" style="left:230px;top:114px;width:130px;height:5px;background:#555"></div><div class="abs" style="left:230px;top:114px;width:55px;height:5px;background:var(--blue3)"></div><div class="abs" style="left:352px;top:108px;font-size:4px;background:#333;color:#fff;padding:1px 2px">45%</div>
  <div class="abs t" style="left:230px;top:132px">Insert Text Here</div>
  <div class="abs" style="left:230px;top:142px;width:130px;height:5px;background:#555"></div><div class="abs" style="left:230px;top:142px;width:120px;height:5px;background:var(--purple3)"></div><div class="abs" style="left:352px;top:136px;font-size:4px;background:#333;color:#fff;padding:1px 2px">90%</div>
  <div class="pg">25</div>
</section>

<!-- 26 Contact -->
<section class="slide">
  <div class="abs" style="left:175px;top:0;width:215px;height:219px;background:linear-gradient(160deg,#2d5f98,#1c4f8c)"></div>
  <div class="abs" style="left:10px;top:105px;width:90px;height:40px;background:#eee"></div>
  <div class="abs" style="left:18px;top:70px;font-size:15px;font-weight:700;color:var(--blue2)">Contact</div>
  <div class="abs" style="left:100px;top:60px;width:14px;height:14px;background:var(--teal)"></div>
  <div class="abs t" style="left:18px;top:92px;width:140px">Lorem ipsum dolor sit amet, consectetur adipiscing elit. Presentation that is beautifully designed.</div>
  <div class="abs" style="left:180px;top:30px;width:14px;height:14px;border-radius:50%;background:var(--blue3)"></div>
  <div class="abs" style="left:180px;top:64px;width:14px;height:14px;border-radius:50%;background:var(--blue3)"></div>
  <div class="abs" style="left:180px;top:98px;width:14px;height:14px;border-radius:50%;background:var(--blue3)"></div>
  <div class="abs" style="left:205px;top:34px;font-size:6px;color:#fff">email@mailbox.com</div>
  <div class="abs" style="left:205px;top:68px;font-size:6px;color:#fff">www.website.com</div>
  <div class="abs t" style="left:205px;top:98px;width:150px;color:#fff">Lorem ipsum dolor sit amet, consectetur adipiscing elit.</div>
  <div class="abs" style="left:200px;top:52px;width:170px;height:1px;background:rgba(255,255,255,.3)"></div>
  <div class="abs" style="left:200px;top:86px;width:170px;height:1px;background:rgba(255,255,255,.3)"></div>
</section>
</div>

<!-- Business cards -->
<div class="band"></div>

<div class="card card-front" style="left:24px;top:2065px">
  <div class="abs" style="left:82px;top:20px;width:1px;height:283px;background:#bbb"></div>
  <div class="abs" style="left:82px;top:100px;width:250px;height:1px;background:#ccc"></div>
  <div class="abs" style="left:82px;top:168px;width:250px;height:1px;background:#ccc"></div>
  <div class="abs" style="left:82px;top:238px;width:250px;height:1px;background:#ccc"></div>
  <svg class="abs" style="left:40px;top:44px" width="22" height="22"><circle cx="11" cy="7" r="5" fill="#333"/><path d="M2 21c0-6 4-9 9-9s9 3 9 9z" fill="#333"/></svg>
  <svg class="abs" style="left:40px;top:122px" width="22" height="22"><path d="M3 9c0-4 16-4 16 0v2h-4V9H7v2H3z" fill="#333"/><rect x="5" y="12" width="12" height="8" rx="1" fill="#333"/><circle cx="11" cy="16" r="2" fill="#fff"/></svg>
  <svg class="abs" style="left:40px;top:192px" width="22" height="22"><circle cx="11" cy="11" r="9" fill="none" stroke="#333" stroke-width="1.8"/><ellipse cx="11" cy="11" rx="4" ry="9" fill="none" stroke="#333" stroke-width="1.5"/><line x1="2" y1="11" x2="20" y2="11" stroke="#333" stroke-width="1.5"/></svg>
  <svg class="abs" style="left:40px;top:262px" width="22" height="22"><path d="M11 2L1 11h3v9h5v-6h4v6h5v-9h3z" fill="#333"/></svg>
  <div class="abs" style="left:100px;top:38px;font-size:22px;font-weight:300;color:var(--navy)">DANIEL REYES</div>
  <div class="abs" style="left:100px;top:66px;font-size:13px;color:#333">Solution Manager</div>
  <div class="abs" style="left:100px;top:114px;font-size:13px;line-height:1.5;color:#333">+18 2000 5550 1234<br>+18 2000 5550 1235</div>
  <div class="abs" style="left:100px;top:184px;font-size:13px;line-height:1.5;color:#333">www.almbergbio.com<br>hello@almbergbio.com</div>
  <div class="abs" style="left:100px;top:254px;font-size:13px;line-height:1.5;color:#333">Street Address Here<br>Lakeside, 2222</div>
  <div class="abs" style="left:345px;top:138px;width:190px;text-align:center">
    <div style="width:22px;height:22px;border-radius:50%;background:var(--blue2);margin:0 auto 6px"></div>
    <div style="font-size:26px;font-weight:700;color:var(--navy);line-height:1">ALMBERG</div>
    <div style="font-size:12px;font-weight:700;color:var(--navy);margin-top:4px">BioRepro Labs</div>
  </div>
</div>

<div class="card card-back" style="left:624px;top:2065px">
  <div class="abs" style="left:0;right:0;top:95px;text-align:center">
    <div style="width:36px;height:36px;border-radius:50%;background:var(--blue2);margin:0 auto 10px"></div>
    <div style="font-size:46px;font-weight:700;color:var(--navy);line-height:1">ALMBERG</div>
    <div style="font-size:20px;font-weight:700;color:var(--navy);margin-top:6px">BioRepro Labs</div>
  </div>
  <svg class="abs" style="left:0;bottom:0" width="548" height="60"><polygon points="0,10 330,10 300,40 0,40" fill="var(--navy)"/><rect x="0" y="36" width="548" height="24" fill="var(--blue3)"/></svg>
</div>

</body>
</html>
```